Dental Specialist Needs a Business Card

We are a state of the art dental specialty office and need a business card that looks modern but professional.
I have provided our logo design in both vertical and horizontal. We use the design on letterhead in the vertical format but provided both forms for you. Thanks
Updates

Please add the address, phone and fax numbers I listed to all designs and please leave a space for website and for my employee name on each design. Thanks 2847 Marlow Avenue, Suite K East Brantham, NY 14391 Phone (716)392-5174 Fax:(716)392-5179 My name is Devin R.Holloway,D.D.S. If you want to show it with my name but the design needs to allow for the name to be switched.

Industry/Entity Type

Business

```html
<!DOCTYPE html>
<html lang="en">
<head>
<meta charset="utf-8">
<title>Keystone Endodontics PC – Business Card</title>
<link rel="stylesheet" href="https://fonts.googleapis.com/css2?family=Lato:wght@300;400;700&display=swap">
<style>
  :root {
    --stage: #e6e6e4;
    --card: #f5f5f3;
    --ink: #2a2a2a;
    --ink-soft: #3c3c3c;
    --brand-blue: #3fa0dc;
    --brand-green: #7cc242;
    --rule-green: #8fbf6a;
    --rule-dark: #333333;
  }
  * { margin: 0; padding: 0; box-sizing: border-box; }
  html, body {
    width: 1200px;
    height: 678px;
    overflow: hidden;
    background: var(--stage);
    font-family: "Lato", sans-serif;
  }
  .business-card {
    position: absolute;
    left: 180px;
    top: 99px;
    width: 840px;
    height: 480px;
    background: var(--card);
    border-radius: 20px;
    box-shadow: 0 2px 10px rgba(0,0,0,0.12);
    overflow: hidden;
    color: var(--ink);
  }
  .corner-swoosh {
    position: absolute;
    right: 0;
    top: 0;
    width: 840px;
    height: 480px;
  }
  .brand {
    position: absolute;
    left: 80px;
    top: 218px;
    display: flex;
    align-items: center;
    gap: 14px;
  }
  .brand-dot {
    width: 30px;
    height: 30px;
    border-radius: 50%;
    background: var(--brand-blue);
  }
  .brand-name {
    font-weight: 700;
    font-size: 25px;
    color: var(--ink);
    letter-spacing: 0.3px;
    white-space: nowrap;
  }
  .divider {
    position: absolute;
    left: 430px;
    top: 150px;
    width: 1.5px;
    height: 170px;
    background: var(--rule-green);
  }
  .contact {
    position: absolute;
    left: 455px;
    top: 150px;
    font-size: 19px;
    line-height: 30px;
    font-weight: 300;
    color: var(--ink-soft);
  }
  .contact .person-name {
    font-weight: 700;
    font-size: 22px;
    color: var(--ink);
  }
  .contact .person-title { font-weight: 400; }
  .contact .address { margin-top: 4px; }
  .web-row {
    position: absolute;
    left: 300px;
    top: 402px;
    width: 510px;
    display: flex;
    align-items: center;
    gap: 16px;
  }
  .web-row .rule {
    flex: 1;
    height: 1.5px;
    background: var(--rule-dark);
  }
  .web-row .website {
    font-size: 22px;
    font-weight: 400;
    color: var(--ink);
    white-space: nowrap;
  }
</style>
</head>
<body>
  <div class="business-card">
    <svg class="corner-swoosh" viewBox="0 0 840 480" aria-hidden="true">
      <path d="M520 0 H700 C730 45 790 42 840 40 V92 C720 98 600 72 520 0 Z" fill="var(--brand-blue)"/>
      <path d="M520 0 C600 84 730 116 840 114 V150 C700 152 580 96 520 0 Z" fill="var(--brand-green)"/>
    </svg>

    <div class="brand">
      <span class="brand-dot"></span>
      <span class="brand-name">Keystone Endodontics PC</span>
    </div>

    <div class="divider"></div>

    <div class="contact">
      <div class="person-name">Marcus Whitley</div>
      <div class="person-title">President</div>
      <div class="phone">555.204.7319</div>
      <div class="email">mwhitley@keystoneendo.com</div>
      <div class="address">Dummy Marlow Ave, Suite 000</div>
      <div class="city">East Brantham, dummy Zipcode</div>
    </div>

    <div class="web-row">
      <span class="rule"></span>
      <span class="website">www.keystoneendo.com</span>
      <span class="rule"></span>
    </div>
  </div>
</body>
</html>
```